Raising Far Ridge Stewards (Book cover)

This project is for a book I am currently writing. It will help pastors and church leaders communicate why serving in the local church is the so important and how to motivate them to serve at high levels.

The title of the book comes from the passage of scripture where Jesus said, "when a solider demands you to carry his gear one mile, go with him two." He wants his followers to willingly do more than is expected. Doing the minimum seldom does much to change hearts of people around us.

This book will deal with these concepts and help leaders train others to follow in this line of thinking - to be Far Ridge Stewards.

Target Market(s)

church leaders, christian book readers

Industry/Entity Type

Church

Font styles to use
Sans Serif

Colors
fece3e

Requirements
Must have
• Catchy color, font layout to attract readers to take a 2nd look inside the book. Lots of empty space on the cover art, gradient color, sharp contrasts. Large Letters
Nice to have
• A central image on the artwork that will communicate the metaphor of going the 2nd mile.
Should not have
• any imagery that is suggestive

```html
<!DOCTYPE html>
<html lang="en">
<head>
<meta charset="utf-8">
<title>Far Ridge Stewards — Book Cover</title>
<link href="https://fonts.googleapis.com/css2?family=Rubik+Dirt&family=Aladin&family=Black+Ops+One&display=swap" rel="stylesheet">
<style>
  :root {
    --title-yellow: #fece3e;
    --ink: #1a1308;
    --rust: #b4552c;
    --deep: #1c1507;
    --umber: #4a3810;
    --gold: #8a6a1c;
  }
  html, body {
    margin: 0;
    padding: 0;
    width: 750px;
    height: 1200px;
    overflow: hidden;
    background: var(--deep);
  }
  .cover {
    position: relative;
    width: 750px;
    height: 1200px;
    overflow: hidden;
  }
  .backdrop {
    position: absolute;
    inset: 0;
    background:
      radial-gradient(ellipse 420px 260px at 520px 820px, rgba(201,162,58,0.55), transparent 70%),
      linear-gradient(180deg, #2a2009 0%, #3d2f0e 22%, var(--gold) 52%, #7a5d18 66%, var(--umber) 82%, var(--deep) 100%);
  }
  .cross-pendant {
    position: absolute;
    left: 488px;
    top: 0;
    width: 202px;
    height: 400px;
    background: linear-gradient(180deg, rgba(60,45,20,0.25) 0%, rgba(176,112,48,0.45) 40%, rgba(150,90,35,0.35) 100%);
    border-radius: 6px;
  }
  .candle-scene {
    position: absolute;
    left: 0;
    top: 768px;
    width: 750px;
    height: 432px;
    background:
      radial-gradient(ellipse 110px 140px at 522px 80px, rgba(255,236,170,0.55), transparent 70%),
      linear-gradient(180deg, transparent 0%, rgba(30,22,8,0.3) 45%, rgba(20,15,5,0.55) 100%);
  }
  .title {
    position: absolute;
    left: 20px;
    top: 66px;
    margin: 0;
    font-family: "Rubik Dirt", "Black Ops One", sans-serif;
    font-weight: 400;
    font-size: 130px;
    color: var(--title-yellow);
    line-height: 1;
    letter-spacing: -4px;
    text-transform: uppercase;
  }
  .title span { display: block; }
  .title .line-2 { margin-top: 50px; }
  .title .line-3 { margin-top: 54px; }
  .scripture {
    position: absolute;
    left: 24px;
    right: 24px;
    top: 612px;
    margin: 0;
    font-family: "Aladin", cursive;
    color: var(--ink);
  }
  .scripture .quote {
    display: block;
    font-size: 27px;
    text-align: center;
    white-space: nowrap;
  }
  .scripture .attribution {
    display: block;
    text-align: right;
    font-style: normal;
    font-size: 48px;
    margin-top: 8px;
    padding-right: 2px;
  }
  .author {
    position: absolute;
    left: 26px;
    right: 26px;
    top: 1138px;
    margin: 0;
    display: flex;
    justify-content: space-between;
    font-family: "Black Ops One", sans-serif;
    font-size: 34px;
    color: var(--rust);
  }
</style>
</head>
<body>
  <main class="cover">
    <div class="backdrop" role="img" aria-label="Dark golden photograph background with soft horizontal blur"></div>
    <div class="cross-pendant" role="img" aria-label="Wooden cross pendant hanging on a cord"></div>
    <div class="candle-scene" role="img" aria-label="Lit tealight candle in a glass holder among dark candle dishes"></div>

    <h1 class="title">
      <span class="line-1">Far</span>
      <span class="line-2">Ridge</span>
      <span class="line-3">Stewards</span>
    </h1>

    <blockquote class="scripture">
      <span class="quote">"when a solider demands you to carry his gear one mile, go with him two"</span>
      <cite class="attribution">- Elder Aldo Venn</cite>
    </blockquote>

    <p class="author">
      <span>A</span><span>U</span><span>T</span><span>H</span><span>O</span><span>R</span><span>N</span><span>A</span><span>M</span><span>E</span>
    </p>
  </main>
</body>
</html>
```